Delia Morvan
exclusive handcrafted jewelry
Simple
delmorvan@quillbox.net
deliamorvandesign.net
business card should be shaded black like uploaded logo.
I also like the royal blue option !
I have no idea what is on that file since I can not open it . I hope it is my logo in blue or shaded black.

```html
<!DOCTYPE html>
<html lang="en">
<head>
<meta charset="utf-8">
<title>Delia Morvan — Stationery</title>
<link rel="stylesheet" href="https://fonts.googleapis.com/css2?family=Lato:wght@300;400&display=swap">
<style>
  :root {
    --backdrop: #3b3b3d;
    --navy-light: #2b2b68;
    --navy: #1d1d4c;
    --navy-deep: #121233;
    --paper: #ffffff;
    --ink-grey: #6f6f74;
    --ink-light: #e6e6f0;
  }
  * { margin: 0; padding: 0; box-sizing: border-box; }
  html, body { width: 1200px; height: 766px; overflow: hidden; background: var(--backdrop); }
  body { font-family: "Lato", Arial, sans-serif; }
  .canvas { position: relative; width: 1200px; height: 766px; }

  .brand-name {
    font-family: "Lato", Arial, sans-serif;
    font-weight: 300;
    letter-spacing: 0.06em;
    white-space: nowrap;
  }

  /* Letterhead */
  .letterhead {
    position: absolute; left: 221px; top: 8px; width: 336px; height: 682px;
    background: var(--paper);
    box-shadow: 0 6px 18px rgba(0,0,0,0.45);
  }
  .letterhead .brand-name {
    position: absolute; top: 78px; left: 0; width: 100%;
    text-align: center; font-size: 22px; color: var(--ink-grey);
  }
  .letterhead-footer {
    position: absolute; left: 0; bottom: 0; width: 100%; height: 22px;
    background: linear-gradient(var(--navy-light), var(--navy-deep));
    color: var(--ink-light); font-size: 7px;
    display: flex; align-items: center; justify-content: center; gap: 10px;
  }

  /* Business card */
  .business-card {
    position: absolute; left: 48px; top: 305px; width: 300px; height: 158px;
    border-radius: 12px;
    background: radial-gradient(ellipse at 35% 35%, var(--navy-light), var(--navy) 55%, var(--navy-deep));
    box-shadow: 0 6px 16px rgba(0,0,0,0.5);
    color: var(--ink-light);
  }
  .business-card .brand-name {
    position: absolute; left: 38px; top: 50px; font-size: 21px; color: var(--paper);
  }
  .card-contact {
    position: absolute; left: 38px; top: 92px; font-size: 7.5px;
    display: flex; gap: 10px;
  }
  .card-web {
    position: absolute; left: 38px; bottom: 12px; font-size: 7.5px; letter-spacing: 0.04em;
  }

  .contact-item { display: inline-flex; align-items: center; gap: 3px; }
  .contact-item svg { width: 7px; height: 7px; fill: currentColor; }

  /* Envelope */
  .envelope {
    position: absolute; left: 581px; top: 262px; width: 552px; height: 334px;
    filter: drop-shadow(0 6px 14px rgba(0,0,0,0.5));
  }
  .envelope-body {
    position: absolute; left: 0; top: 58px; width: 552px; height: 276px; background: var(--paper);
  }
  .envelope-flap { position: absolute; left: 0; top: 0; width: 552px; height: 100px; }
  .envelope-flap .brand-name {
    position: absolute; top: 34px; left: 0; width: 100%; text-align: center;
    font-size: 17px; color: var(--ink-light);
  }
  .envelope-return {
    position: absolute; left: 24px; top: 112px; font-size: 18px; color: var(--ink-grey);
  }
  .envelope-footer {
    position: absolute; left: 0; bottom: 0; width: 100%; height: 22px;
    background: linear-gradient(var(--navy-light), var(--navy-deep));
    color: var(--ink-light); font-size: 7px;
    display: flex; align-items: center; justify-content: flex-start; padding-left: 28px; gap: 10px;
  }
</style>
</head>
<body>
<main class="canvas">

  <section class="letterhead" aria-label="Letterhead">
    <p class="brand-name">Delia Morvan</p>
    <footer class="letterhead-footer">
      <span class="contact-item"><svg viewBox="0 0 10 10"><path d="M2 1l2 2-1 1.5c.6 1.2 1.3 1.9 2.5 2.5L7 6l2 2-1.5 1.5C4.5 9 1 5.5.5 2.5z"/></svg>555-210-3384</span>
      <span class="contact-item"><svg viewBox="0 0 10 10"><rect x="0.5" y="2" width="9" height="6" rx="1"/></svg>delmorvan@quillbox.net</span>
      <span class="contact-item"><svg viewBox="0 0 10 10"><circle cx="5" cy="5" r="4.5"/></svg>www.deliamorvandesign.net</span>
    </footer>
  </section>

  <section class="business-card" aria-label="Business card">
    <p class="brand-name">Delia Morvan</p>
    <div class="card-contact">
      <span class="contact-item"><svg viewBox="0 0 10 10"><path d="M2 1l2 2-1 1.5c.6 1.2 1.3 1.9 2.5 2.5L7 6l2 2-1.5 1.5C4.5 9 1 5.5.5 2.5z"/></svg>555-210-3384</span>
      <span class="contact-item"><svg viewBox="0 0 10 10"><rect x="0.5" y="2" width="9" height="6" rx="1"/></svg>delmorvan@quillbox.net</span>
    </div>
    <p class="card-web">www.deliamorvandesign.net</p>
  </section>

  <section class="envelope" aria-label="Envelope">
    <div class="envelope-body"></div>
    <svg class="envelope-flap" viewBox="0 0 552 100" aria-hidden="true">
      <defs>
        <linearGradient id="flap-shade" x1="0" y1="0" x2="0" y2="1">
          <stop offset="0" stop-color="var(--navy-light)"/>
          <stop offset="1" stop-color="var(--navy-deep)"/>
        </linearGradient>
      </defs>
      <path d="M0 58 Q0 22 40 18 Q276 -14 512 18 Q552 22 552 58 L552 96 Q276 70 0 96 Z" fill="url(#flap-shade)"/>
    </svg>
    <div class="envelope-flap"><p class="brand-name">Delia Morvan</p></div>
    <p class="envelope-return brand-name">Delia Morvan</p>
    <footer class="envelope-footer">
      <span class="contact-item"><svg viewBox="0 0 10 10"><path d="M2 1l2 2-1 1.5c.6 1.2 1.3 1.9 2.5 2.5L7 6l2 2-1.5 1.5C4.5 9 1 5.5.5 2.5z"/></svg>555-210-3384</span>
      <span class="contact-item"><svg viewBox="0 0 10 10"><rect x="0.5" y="2" width="9" height="6" rx="1"/></svg>delmorvan@quillbox.net</span>
      <span class="contact-item"><svg viewBox="0 0 10 10"><circle cx="5" cy="5" r="4.5"/></svg>www.deliamorvandesign.net</span>
    </footer>
  </section>

</main>
</body>
</html>
```